Business Card Design

Two women who are flipping houses. Want the women with sledge hammers and in work boots. Liked the ones for cleaning with the woman but just needs some modifications to the women. On the back, I want both of our names and phone numbers.

Rosalind Halvorsen
214-803-5127

Bettina Halvorsen
312-908-2741

Business

NAILED IT TWICE!!!!

```html
<!DOCTYPE html>
<html lang="en">
<head>
<meta charset="utf-8">
<title>Halvorsen Business Cards</title>
<link rel="stylesheet" href="https://fonts.googleapis.com/css2?family=Oswald:wght@700&family=Arimo:wght@700&display=swap">
<style>
  :root {
    --page: #eceae6;
    --card: #ffffff;
    --navy: #1b4673;
    --name-blue: #1f4e8c;
    --ink: #111111;
    --sky-light: #bfe3fb;
    --sky: #4fa6e8;
    --sky-deep: #1f6fc0;
    --worker-tone: #d9c9a3;
  }
  * { margin: 0; padding: 0; box-sizing: border-box; }
  html, body { width: 1200px; height: 784px; overflow: hidden; background: var(--page); }
  .sheet {
    position: relative; width: 1200px; height: 784px;
    display: flex; align-items: center; justify-content: center; gap: 40px;
  }
  .card {
    position: relative; width: 540px; height: 309px;
    background: var(--card); overflow: hidden;
    box-shadow: 0 6px 18px rgba(0,0,0,0.18);
  }
  /* Back: names and numbers */
  .contacts {
    position: absolute; left: 40px; top: 78px; width: 290px;
    text-align: center; font-family: "Arimo", Arial, sans-serif; font-weight: 700;
  }
  .contact + .contact { margin-top: 34px; }
  .contact-name { color: var(--name-blue); font-size: 19px; letter-spacing: 0.2px; }
  .contact-phone { color: var(--ink); font-size: 19px; margin-top: 6px; letter-spacing: 0.5px; }
  .flow-ribbon { position: absolute; left: 330px; top: 0; width: 140px; height: 309px; }
  /* Front: headline and imagery */
  .front-glow {
    position: absolute; right: 0; top: 0; width: 330px; height: 309px;
    background: linear-gradient(90deg, rgba(255,255,255,0) 0%, var(--sky-light) 18%, var(--sky) 55%, var(--sky-deep) 100%);
  }
  .headline {
    position: absolute; left: 190px; top: 30px;
    font-family: "Oswald", "Arial Narrow", sans-serif; font-weight: 700;
    font-size: 38px; line-height: 1; color: var(--navy);
    letter-spacing: 0.5px; transform: scaleY(1.15); transform-origin: left top;
  }
  .worker {
    position: absolute; left: 70px; top: 46px; width: 170px; height: 263px;
    background: linear-gradient(180deg, #f1ead8 0%, var(--worker-tone) 100%);
    border-radius: 60px 60px 0 0;
  }
</style>
</head>
<body>
<main class="sheet">
  <section class="card card-back">
    <div class="contacts">
      <div class="contact">
        <p class="contact-name">Rosalind Halvorsen</p>
        <p class="contact-phone">214-803-5127</p>
      </div>
      <div class="contact">
        <p class="contact-name">Bettina Halvorsen</p>
        <p class="contact-phone">312-908-2741</p>
      </div>
    </div>
    <svg class="flow-ribbon" viewBox="0 0 140 309" role="img" aria-label="Flowing blue abstract ribbon">
      <defs>
        <linearGradient id="ribbonFill" x1="0" y1="0" x2="1" y2="1">
          <stop offset="0" stop-color="#2c7fd6"/>
          <stop offset="0.5" stop-color="#8cc9f3"/>
          <stop offset="1" stop-color="#3a8fdc"/>
        </linearGradient>
      </defs>
      <path d="M58 0 C40 50 80 80 60 130 C40 180 90 200 70 250 C60 280 60 300 62 309 L118 309 C110 270 130 230 112 190 C96 150 128 110 110 60 C104 35 112 15 118 0 Z" fill="url(#ribbonFill)"/>
    </svg>
  </section>

  <section class="card card-front">
    <div class="front-glow" role="img" aria-label="Bright blue abstract light streaks"></div>
    <div class="worker" role="img" aria-label="Illustration of a woman in hard hat and safety vest holding a sledgehammer"></div>
    <h1 class="headline">NAILED IT TWICE!!!!</h1>
  </section>
</main>
</body>
</html>
```